Brochure for Varesh Law firm

We would like to have a brochure that describes the Firm ( about the firm) , the vision, the team , the practice areas. And the contact.
Varesh law firm has ranked as top Libyan law firms by Juris Ledger.
It will give a good picture if you look at www.varesh-example.ly

We can also provide more information if requested to share with designer.

```html
<!DOCTYPE html>
<html lang="en">
<head>
<meta charset="utf-8">
<title>Varesh Law firm – Brochure</title>
<link rel="stylesheet" href="https://fonts.googleapis.com/css2?family=Montserrat:wght@300;400;500;600;700;800&family=Open+Sans:wght@400;600&display=swap">
<style>
:root{
  --blue:#0a45b0;
  --blue-deep:#0638a0;
  --ink:#1a1a1a;
  --paper:#ffffff;
  --mist:#eef0f3;
  --line:#cfd3da;
  --stage:#5a5a5a;
}
*{margin:0;padding:0;box-sizing:border-box}
html,body{width:828px;height:1200px;overflow:hidden}
body{background:var(--stage);font-family:"Montserrat",sans-serif;color:var(--ink);position:relative}
.sheet{position:absolute;left:94px;width:640px;height:452px;background:var(--paper);overflow:hidden}
.sheet--outer{top:99px}
.sheet--inner{top:645px}
.panel{position:absolute;top:0;width:213.3px;height:452px;overflow:hidden}
.p1{left:0}.p2{left:213.3px}.p3{left:426.6px}
.shape{position:absolute;inset:0;width:100%;height:100%}
.abs{position:absolute}
.body-copy{font-family:"Open Sans",sans-serif}

/* outer panel 1 */
.intro{left:22px;top:25px;width:170px;color:#fff;font-size:7px;line-height:9px;font-family:"Open Sans",sans-serif;letter-spacing:-.1px}
.photo-frame{left:22px;top:90px;width:168px;height:183px;background:#fff;padding:4px}
.photo-frame div{width:100%;height:100%;background:linear-gradient(160deg,#8a8a8a,#3a3a3a 55%,#6a6a6a)}
.clients-title{left:21px;top:287px;color:var(--blue);font-weight:700;font-size:16px}
.client-grid{left:22px;top:315px;display:grid;grid-template-columns:repeat(3,54px);grid-auto-rows:37px;gap:3.5px}
.client{background:#f2f2f2;border:1px solid #dcdcdc;display:flex;align-items:center;justify-content:center;font-size:7px;font-weight:600;color:#555;text-align:center}

/* testimonials */
.t-kicker{left:27px;top:24px;font-size:15px;font-weight:300}
.t-title{left:27px;top:41px;font-size:15px;font-weight:700;color:var(--blue)}
.rule{height:1px;background:var(--blue)}
.rule--white{background:#fff}
.quote{left:29px;width:159px;font-size:5.8px;line-height:7.8px;text-align:justify;font-family:"Open Sans",sans-serif}
.quote .mark{font-family:"Montserrat",sans-serif;font-size:22px;font-weight:800;color:#aaa;line-height:6px;vertical-align:-8px;margin-right:2px}
.source{left:128px;font-size:7px;font-weight:600;color:var(--blue);display:flex;align-items:center;gap:4px}
.source .mark{font-size:22px;font-weight:800;color:#aaa;line-height:10px;padding-top:6px}
.contact-title{left:28px;top:318px;color:#fff;font-size:16px;font-weight:300}
.contact-title b{font-weight:700}
.office{color:#fff;font-size:6.5px;line-height:8px}
.office h4{font-size:7px;font-weight:700;margin-bottom:3px}
.office p{display:flex;gap:3px;font-weight:500}
.office svg{flex:none;margin-top:1px}
.url{color:#fff;font-weight:600;display:flex;align-items:center;gap:4px}

/* cover */
.wordmark{left:29px;top:22px;font-size:34px;font-weight:600;letter-spacing:-.5px;color:var(--ink)}
.cover-title{left:29px;top:297px;color:#fff;font-size:20px;font-weight:800;line-height:26px}
.cover-tag{left:29px;top:379px;color:#fff;font-size:8.5px;font-weight:500;line-height:11px}

/* services */
.svc-heading{left:29px;top:26px;color:#fff;font-size:16px;font-weight:300}
.svc-heading b{font-weight:700}
.svc{position:absolute;left:32px;display:flex;gap:9px;color:#fff}
.svc .ico{flex:none;width:33px;height:33px;border-radius:50%;background:#fff;display:flex;align-items:center;justify-content:center;box-shadow:-4px 4px 6px rgba(0,0,0,.25)}
.svc h3{font-size:9.5px;font-weight:700;margin-top:4px}
.svc p{font-size:6.5px;line-height:8px;font-weight:500;width:125px;margin-top:1px}
.photo-band{left:0;top:271px;width:426.6px;height:181px;background:linear-gradient(100deg,#d9cfc2,#eef1f5 35%,#cbd6e6 55%,#e6ddd2 80%,#b8aa98)}

/* IP panel */
.ip-bg{background:linear-gradient(180deg,#f7f7f7,#e9eaec)}
.ip-kicker{left:27px;top:27px;font-size:16px;font-weight:300}
.ip-title{left:27px;top:45px;font-size:16px;font-weight:700;color:var(--blue);line-height:21px}
.ip-copy{left:28px;top:110px;width:160px;font-size:7px;line-height:9.2px;font-weight:500}
.ip{position:absolute;left:29px;display:flex;gap:7px}
.ip .disc{flex:none;width:33px;height:33px;border-radius:50%;background:var(--blue);border:2px solid #fff;box-shadow:-4px 4px 6px rgba(0,0,0,.2);color:#fff;font-weight:700;font-size:11px;display:flex;align-items:center;justify-content:center}
.ip h3{font-size:9.5px;font-weight:700;color:var(--blue);margin-top:1px}
.ip p{font-size:6.5px;line-height:8px;font-weight:500;width:125px;margin-top:1px}
.ip-cta{left:28px;top:418px;color:var(--blue);font-size:9px;font-weight:700}
</style>
</head>
<body>

<!-- OUTER SIDE -->
<section class="sheet sheet--outer">
  <div class="panel p1">
    <svg class="shape" viewBox="0 0 213 452" preserveAspectRatio="none" aria-hidden="true">
      <polygon points="0,0 213,0 213,171 0,217" fill="var(--blue)"/>
      <polygon points="0,0 213,0 213,20 0,40" fill="#fff" opacity=".05"/>
    </svg>
    <p class="abs intro">Varesh Law is a law firm established in Tripoli, Libya, in 2005. The Firm brings together some of the most experienced legal practitioners and scholars in Libya. In addition to our head offices in Tripoli, our first regional office was launched in Benghazi.</p>
    <div class="abs photo-frame"><div role="img" aria-label="Black and white photograph of ancient stone arches"></div></div>
    <h2 class="abs clients-title">Clients</h2>
    <div class="abs client-grid">
      <div class="client">Corvana</div>
      <div class="client">Helix Power</div>
      <div class="client">Norvik</div>
      <div class="client">Petralis</div>
      <div class="client">Netbridge</div>
      <div class="client">Oakline</div>
      <div class="client">Searchly</div>
      <div class="client">Harbor Bank</div>
      <div class="client">Mardon Energy</div>
    </div>
  </div>

  <div class="panel p2">
    <svg class="shape" viewBox="0 0 213 452" preserveAspectRatio="none" aria-hidden="true">
      <polygon points="0,306 213,256 213,452 0,452" fill="var(--blue)"/>
      <polygon points="120,452 213,395 213,452" fill="#fff" opacity=".08"/>
      <polygon points="30,272 30,312 66,290" fill="#444"/>
      <polygon points="43,298 43,310 53,304" fill="#fff"/>
    </svg>
    <p class="abs t-kicker">Clients’</p>
    <h2 class="abs t-title">Testimonials</h2>
    <div class="abs rule" style="left:28px;top:63px;width:156px"></div>

    <p class="abs quote" style="top:72px"><span class="mark">“</span>Varesh Law operates in a genuine niche as a law firm providing international law firm levels of support and responsiveness in connection with the Libyan jurisdiction.</p>
    <div class="abs source" style="top:104px">Juris Ledger <span class="mark">”</span></div>

    <p class="abs quote" style="top:124px"><span class="mark">“</span>Samir Haddad has unrivalled expertise in the Libyan legal market. He also has excellent local knowledge which informs his legal advice. We consider Varesh to be the premier law firm in this market.</p>
    <div class="abs source" style="top:163px">Juris Ledger <span class="mark">”</span></div>

    <p class="abs quote" style="top:183px"><span class="mark">“</span>In-depth knowledge of Libyan laws and regulations… practical know-how of how the Libyan public sector actually functions In Libya, the procedural, registration and documentary requirements associated with a transaction are often opaque and it is essential to seek guidance from an adviser who can offer more than a purely written analysis of the laws themselves.</p>
    <div class="abs source" style="top:246px">Juris Ledger <span class="mark">”</span></div>

    <h2 class="abs contact-title">Contact <b>us</b></h2>
    <div class="abs rule rule--white" style="left:28px;top:340px;width:156px"></div>
    <div class="abs office" style="left:28px;top:349px;width:80px">
      <h4>Tripoli Office</h4>
      <p><svg width="6" height="7" viewBox="0 0 6 7"><circle cx="3" cy="2.5" r="1.8" fill="none" stroke="#fff" stroke-width=".8"/><path d="M3 4.3V7" stroke="#fff" stroke-width=".8"/></svg><span>12, Harbour Plaza 3<br>P.O. Box 40120<br>Tripoli, Libya</span></p>
    </div>
    <div class="abs office" style="left:110px;top:349px;width:100px">
      <h4>Benghazi Office</h4>
      <p><svg width="6" height="7" viewBox="0 0 6 7"><circle cx="3" cy="2.5" r="1.8" fill="none" stroke="#fff" stroke-width=".8"/><path d="M3 4.3V7" stroke="#fff" stroke-width=".8"/></svg><span>Shari’ Al Nakheel,<br>Block 7, North District.<br>Benghazi, Libya.</span></p>
    </div>
    <div class="abs office" style="left:28px;top:395px"><p><svg width="7" height="7" viewBox="0 0 7 7"><circle cx="3.5" cy="3.5" r="3" fill="none" stroke="#fff" stroke-width=".7"/><path d="M2.4 2.2l.7-.3.5 1-.5.4.9.9.4-.5 1 .5-.3.7c-1.4.2-2.9-1.3-2.7-2.7z" fill="#fff"/></svg>+218 21 555 0147</p></div>
    <div class="abs office" style="left:101px;top:395px"><p><svg width="7" height="7" viewBox="0 0 7 7"><circle cx="3.5" cy="3.5" r="3" fill="none" stroke="#fff" stroke-width=".7"/><path d="M2.4 2.2l.7-.3.5 1-.5.4.9.9.4-.5 1 .5-.3.7c-1.4.2-2.9-1.3-2.7-2.7z" fill="#fff"/></svg>+218 92 555 0281</p></div>
    <div class="abs rule rule--white" style="left:28px;top:410px;width:156px"></div>
    <p class="abs url" style="left:28px;top:420px;font-size:7.5px"><svg width="7" height="7" viewBox="0 0 7 7"><circle cx="3.5" cy="3.5" r="3" fill="none" stroke="#fff" stroke-width=".7"/><path d="M.5 3.5h6M3.5.5c-1.6 1.8-1.6 4.2 0 6M3.5.5c1.6 1.8 1.6 4.2 0 6" fill="none" stroke="#fff" stroke-width=".6"/></svg>www.varesh-example.ly</p>
  </div>

  <div class="panel p3">
    <svg class="shape" viewBox="0 0 213 452" preserveAspectRatio="none" aria-hidden="true">
      <polygon points="0,256 213,306 213,452 0,452" fill="var(--blue)"/>
      <polygon points="0,109 213,63 213,306 0,256" fill="url(#deskTone)" role="img" aria-label="Photograph of a lawyer in a suit advising a client at a desk with a laptop and gavel"/>
      <polygon points="30,78 30,118 66,98" fill="var(--blue)"/>
      <polygon points="43,104 43,116 53,110" fill="#fff"/>
      <polygon points="183,283 183,313 158,298" fill="#fff"/>
      <polygon points="90,452 213,410 213,452" fill="#fff" opacity=".07"/>
      <defs>
        <linearGradient id="deskTone" x1="0" y1="0" x2="1" y2="1">
          <stop offset="0" stop-color="#2b2f38"/>
          <stop offset=".5" stop-color="#4a4f5a"/>
          <stop offset="1" stop-color="#c9c6c0"/>
        </linearGradient>
      </defs>
    </svg>
    <p class="abs wordmark">Varesh</p>
    <h1 class="abs cover-title">Setting<br>The Standard<br>For Libya</h1>
    <p class="abs cover-tag">Excellence is the<br>hallmark of our legal solutions.</p>
    <div class="abs rule rule--white" style="left:29px;top:410px;width:155px"></div>
    <p class="abs url" style="left:29px;top:418px;font-size:10px"><svg width="9" height="9" viewBox="0 0 7 7"><circle cx="3.5" cy="3.5" r="3" fill="none" stroke="#fff" stroke-width=".7"/><path d="M.5 3.5h6M3.5.5c-1.6 1.8-1.6 4.2 0 6M3.5.5c1.6 1.8 1.6 4.2 0 6" fill="none" stroke="#fff" stroke-width=".6"/></svg>www.varesh-example.ly</p>
  </div>
</section>

<!-- INNER SIDE -->
<section class="sheet sheet--inner">
  <div class="abs" style="left:0;top:0;width:426.6px;height:271px;background:var(--blue)"></div>
  <div class="abs" style="left:213px;top:0;width:1px;height:271px;background:rgba(255,255,255,.12)"></div>
  <div class="abs photo-band" role="img" aria-label="Photograph of a legal team reviewing and signing documents around a meeting table"></div>

  <div class="panel p1">
    <h2 class="abs svc-heading">Varesh Law <b>Services</b></h2>
    <div class="abs rule rule--white" style="left:29px;top:51px;width:155px"></div>
    <div class="svc" style="top:66px"><span class="ico"><svg width="18" height="18" viewBox="0 0 18 18" fill="none" stroke="var(--blue)" stroke-width="1"><circle cx="5" cy="5" r="2"/><circle cx="13" cy="5" r="2"/><circle cx="9" cy="7" r="2"/><path d="M2 16v-5h6M10 11h6v5M6 16v-4h6v4"/></svg></span><div><h3>Consultation</h3><p>Varesh provides consultation legal practice in Libya</p></div></div>
    <div class="svc" style="top:115px"><span class="ico"><svg width="18" height="18" viewBox="0 0 18 18" fill="none" stroke="var(--blue)" stroke-width="1.1"><path d="M4 4l5-3 2 3-5 3z"/><path d="M8 6l7 7-1.5 1.5-7-7"/><path d="M1 16h8"/></svg></span><div><h3>Litigation</h3><p>Varesh provides Litigation practice in Libya</p></div></div>
    <div class="svc" style="top:164px"><span class="ico"><svg width="18" height="18" viewBox="0 0 18 18" fill="none" stroke="var(--blue)" stroke-width="1"><path d="M9 2v13M3 4h12M5 15h8"/><path d="M3 4l-2 5h4zM15 4l-2 5h4z"/></svg></span><div><h3>Arbitration</h3><p>Varesh provides arbitration legal practice in Libya</p></div></div>
    <div class="svc" style="top:213px"><span class="ico"><svg width="18" height="18" viewBox="0 0 18 18" fill="none" stroke="var(--blue)" stroke-width="1"><rect x="4" y="2" width="10" height="14"/><path d="M6 5h6M6 8h6M6 11h6M6 13h4"/></svg></span><div><h3>Commercial Registration</h3><p>Varesh provides commercial registration services in Libya</p></div></div>
  </div>

  <div class="panel p2">
    <div class="svc" style="top:66px"><span class="ico"><svg width="18" height="18" viewBox="0 0 18 18" fill="none" stroke="var(--blue)" stroke-width="1"><rect x="2" y="3" width="12" height="12"/><path d="M4 6h8M4 9h5M4 12h4"/><circle cx="13" cy="12" r="2.5"/></svg></span><div><h3>Investment Licence</h3><p>Varesh provides investment licence services in Libya</p></div></div>
    <div class="svc" style="top:115px"><span class="ico"><svg width="18" height="18" viewBox="0 0 18 18" fill="none" stroke="var(--blue)" stroke-width="1"><rect x="3" y="3" width="10" height="13"/><path d="M6 2h4v2H6zM5 7h6M5 10h6M5 13h3"/><path d="M12 11l3 5h-6z"/></svg></span><div><h3>Legal Risk Assessment</h3><p>Varesh provides legal risk assessment services in Libya</p></div></div>
    <div class="svc" style="top:164px"><span class="ico"><svg width="18" height="18" viewBox="0 0 18 18" fill="none" stroke="var(--blue)" stroke-width="1"><rect x="4" y="2" width="11" height="14" rx="1"/><circle cx="9.5" cy="7" r="2"/><path d="M6.5 13c0-2 6-2 6 0M3 5h2M3 9h2M3 13h2"/></svg></span><div><h3>Due-Diligence</h3><p>Varesh provides due-diligence services in Libya</p></div></div>
    <div class="svc" style="top:213px"><span class="ico"><svg width="18" height="18" viewBox="0 0 18 18" fill="none" stroke="var(--blue)" stroke-width="1"><path d="M9 2l4 1.5v3.5c0 2.5-2 4-4 4.5-2-.5-4-2-4-4.5V3.5z"/><path d="M7 6.5l1.5 1.5L11 5.5"/><path d="M2 9l2 6 3 1M16 9l-2 6-3 1"/></svg></span><div><h3>Intellectual Property</h3><p>Varesh provides intellectual property services in Libya</p></div></div>
  </div>

  <div class="panel p3 ip-bg">
    <p class="abs ip-kicker">Intellectual</p>
    <h2 class="abs ip-title">Property Services<br>in Libya</h2>
    <div class="abs rule" style="left:28px;top:97px;width:156px"></div>
    <p class="abs ip-copy">We offer our clients a full range of IP services, including processing applications for trademark, patent, copyright and design protection, conducting prior art searches, acting in IP litigation, drafting and negotiating IP contracts, and providing consultation spanning across Libyan aspects of intellectual property laws and regulations.</p>
    <div class="ip" style="top:218px"><span class="disc">TM</span><div><h3>Trademark</h3><p>Varesh Firm provides trademark services in Libya</p></div></div>
    <div class="ip" style="top:267px"><span class="disc">P</span><div><h3>Patent</h3><p>Varesh Firm provides patent registration services in Libya</p></div></div>
    <div class="ip" style="top:316px"><span class="disc">C</span><div><h3>Copyright</h3><p>Varesh Firm provides copyright services in Libya</p></div></div>
    <div class="ip" style="top:365px"><span class="disc"><svg width="15" height="15" viewBox="0 0 15 15" fill="none" stroke="#fff" stroke-width="1"><rect x="1.5" y="1.5" width="6" height="6"/><rect x="7.5" y="7.5" width="6" height="6"/><path d="M7.5 4.5h3v3M4.5 7.5v3h3"/></svg></span><div><h3>Addons Services</h3><p>Varesh provides addons services in Libya</p></div></div>
    <p class="abs ip-cta">Ask Varesh Online for Non Corporate</p>
  </div>
</section>

</body>
</html>
```